Velmora business card design

Design a business card for a cryptocurrency company that uses the attached logo. Some example business cards to give you guys a flavor of what we're looking for is given below (of course feel free to be creative):
https://www.plimtorque.com/studio.aspx?template=5813490_KT4&ag=True&xnav=HSG_Design_Image&rd=1
https://www.plimtorque.com/studio.aspx?template=7240615_KT4&ag=True&xnav=HSG_Design_Image&rd=1
The business card should be clean/simple and convey the company name, what we're about and the specific persons contact info. In terms of what we're about, we can have our name Velmora, with a line under it that says "Cryptocurrency visualization, analytics, and trading"
We want something futuristic looking but simple / clean.
The color scheme for the logo should be used.
The name of the person and their title should be editable, so we can use the business card design for multiple people.
(Please use the zip file to get the vector graphics and different image formats)

```html
<!DOCTYPE html>
<html lang="en">
<head>
<meta charset="utf-8">
<title>Velmora business card</title>
<link rel="stylesheet" href="https://fonts.googleapis.com/css2?family=Open+Sans:wght@400;600;700&display=swap">
<style>
  :root {
    --backdrop: #e9e7e3;
    --navy: #0b1b31;
    --paper: #f7f7f6;
    --ink: #14233a;
    --muted: #3a4658;
    --mark: #2f9e88;
    --white: #ffffff;
  }
  * { margin: 0; padding: 0; box-sizing: border-box; }
  html, body {
    width: 1200px;
    height: 800px;
    overflow: hidden;
    background: var(--backdrop);
    font-family: "Open Sans", Arial, sans-serif;
  }
  .stage {
    position: relative;
    width: 1200px;
    height: 800px;
    display: flex;
    align-items: center;
    justify-content: center;
    gap: 60px;
  }
  .card {
    position: relative;
    width: 525px;
    height: 300px;
    border-radius: 4px;
    box-shadow: 0 10px 30px rgba(0,0,0,0.18);
    overflow: hidden;
  }
  .card--front { background: var(--navy); color: var(--white); }
  .card--back { background: var(--paper); color: var(--ink); }

  .brand {
    position: absolute;
    display: flex;
    align-items: center;
  }
  .brand__square {
    background: var(--mark);
    flex: none;
  }
  .brand__name {
    font-weight: 600;
    text-transform: uppercase;
    letter-spacing: 0.06em;
    line-height: 1;
  }
  .card--front .brand { left: 70px; top: 100px; gap: 20px; }
  .card--front .brand__square { width: 62px; height: 62px; }
  .card--front .brand__name { font-size: 50px; color: var(--white); }

  .tagline {
    position: absolute;
    left: 0; right: 0;
    bottom: 34px;
    text-align: center;
    font-size: 13px;
    color: #dfe5ee;
    letter-spacing: 0.01em;
  }

  .card--back .brand { left: 34px; top: 34px; gap: 14px; }
  .card--back .brand__square { width: 44px; height: 44px; }
  .card--back .brand__name { font-size: 36px; color: var(--ink); }

  .person {
    position: absolute;
    left: 36px;
    top: 118px;
  }
  .person__name {
    font-size: 19px;
    font-weight: 700;
    letter-spacing: 0.02em;
  }
  .person__title {
    font-size: 13px;
    color: var(--muted);
    margin-top: 2px;
  }
  .contact {
    position: absolute;
    left: 36px;
    top: 196px;
    list-style: none;
    font-size: 13.5px;
    line-height: 1.4;
    color: var(--ink);
  }
  .corner-square {
    position: absolute;
    right: 40px;
    bottom: 36px;
    width: 130px;
    height: 130px;
    background: var(--mark);
  }
</style>
</head>
<body>
  <main class="stage">
    <section class="card card--front" aria-label="Card front">
      <div class="brand">
        <span class="brand__square"></span>
        <span class="brand__name">Velmora</span>
      </div>
      <p class="tagline">Cryptocurrency visualization, analytics, and trading</p>
    </section>

    <section class="card card--back" aria-label="Card back">
      <div class="brand">
        <span class="brand__square"></span>
        <span class="brand__name">Velmora</span>
      </div>
      <div class="person">
        <p class="person__name">JOHN DOE</p>
        <p class="person__title">Managing Director</p>
      </div>
      <ul class="contact">
        <li>+12 345 6789</li>
        <li>email@domainname.com</li>
        <li>www.domainname.com</li>
      </ul>
      <span class="corner-square"></span>
    </section>
  </main>
</body>
</html>
```